sommelier *

Sommelier Wine Hospitality Corvanne Star experience I'm working as a sommelier in a Corvanne Star restaurant. I try to reach People who are interested in invest in wine and wine loovers! In terms of color I would like to have a nice color based on a nice bordeaux red (as an advice). By the way i forgot to write my phone number and my email address. 439812604731 kdervin7@postiko.com I hope this info is enough so far.

```html
<!DOCTYPE html>
<html lang="en">
<head>
<meta charset="utf-8">
<title>Tobias Renlow – Sommelier Business Cards</title>
<link rel="stylesheet" href="https://fonts.googleapis.com/css2?family=Montserrat:wght@400;500&display=swap">
<style>
  :root {
    --backdrop: #2a2a2c;
    --bordeaux: #6f0f13;
    --bordeaux-deep: #5a0a0e;
    --gold-dark: #9a7418;
    --gold: #d8b233;
    --gold-light: #f1dc4a;
    --ink: #1b1612;
    --paper-white: #ffffff;
    --photo-sky: #f3e2b0;
    --photo-hills: #b89a4a;
    --photo-vines: #6f7a2c;
    --photo-table: #8a5a2a;
  }
  * { margin: 0; padding: 0; box-sizing: border-box; }
  html, body {
    width: 1200px; height: 902px; overflow: hidden;
    background: var(--backdrop);
  }
  .canvas {
    position: relative; width: 1200px; height: 902px;
    display: flex; align-items: center; justify-content: center; gap: 40px;
  }
  .card {
    position: relative; width: 540px; height: 310px;
    border-radius: 18px; overflow: hidden;
    font-family: "Montserrat", sans-serif;
  }
  /* Front card */
  .card--front { background: var(--bordeaux); }
  .card--front .facets { position: absolute; inset: 0; width: 100%; height: 100%; }
  .brand-name {
    position: absolute; display: flex; align-items: center; gap: 14px;
    font-weight: 500; letter-spacing: 1px; white-space: nowrap;
  }
  .brand-name .dot {
    width: 16px; height: 16px; border-radius: 50%;
  }
  .card--front .brand-name {
    left: 58px; top: 116px; font-size: 42px; color: var(--gold-light);
  }
  .card--front .brand-name .dot { background: var(--gold-light); }
  .contact-line {
    position: absolute; left: 58px; top: 196px;
    font-size: 13px; font-weight: 400; letter-spacing: 0.6px;
    color: var(--paper-white);
  }
  /* Back card */
  .card--back .scene-photo {
    position: absolute; inset: 0;
    background:
      linear-gradient(180deg, var(--photo-sky) 0%, #e9cf86 30%, var(--photo-hills) 45%, var(--photo-vines) 65%, var(--photo-table) 100%);
  }
  .card--back .brand-name {
    right: 40px; top: 56px; font-size: 34px; color: var(--ink);
  }
  .card--back .brand-name .dot { background: var(--bordeaux); }
</style>
</head>
<body>
<main class="canvas">
  <section class="card card--front" aria-label="Business card front">
    <svg class="facets" viewBox="0 0 540 310" preserveAspectRatio="none" aria-hidden="true">
      <defs>
        <linearGradient id="goldSweep" x1="0" y1="1" x2="1" y2="0">
          <stop offset="0" stop-color="var(--gold-dark)"/>
          <stop offset="0.6" stop-color="var(--gold)"/>
          <stop offset="1" stop-color="var(--gold-light)"/>
        </linearGradient>
      </defs>
      <rect width="540" height="310" fill="var(--bordeaux)"/>
      <polygon points="0,310 540,140 540,310" fill="var(--bordeaux-deep)" opacity="0.45"/>
      <polygon points="360,0 540,0 540,310 260,310" fill="url(#goldSweep)"/>
      <polygon points="360,0 470,0 330,200" fill="#ffffff" opacity="0.08"/>
      <polygon points="540,60 540,310 420,310" fill="#ffffff" opacity="0.10"/>
      <polygon points="260,310 330,200 400,310" fill="#000000" opacity="0.10"/>
    </svg>
    <div class="brand-name"><span>TOBIAS</span><span class="dot"></span><span>RENLOW</span></div>
    <p class="contact-line">+439 812 604 731 | KDERVIN7@POSTIKO.COM</p>
  </section>

  <section class="card card--back" aria-label="Business card back">
    <div class="scene-photo" role="img" aria-label="Photograph of a wine barrel, a bottle of red wine, grapes and a cork on a table before sunlit vineyard hills"></div>
    <div class="brand-name"><span>TOBIAS</span><span class="dot"></span><span>RENLOW</span></div>
  </section>
</main>
</body>
</html>
```